Business cards for Remote DBA team

Business cards for team offering database administration, consultation, machine learning and AI services. As of now team is using both
www.korvilnet.cz and www.brestmoorlab.cz URLs

Target Market(s)

IT managers

Industry/Entity Type

It Professional

Contact Information for Business Card

Should include logo
name, email, phone, twitter tag

Font styles to use
Sans Serif

Colors

Designer to choose colors to be used in the design.

```html
<!DOCTYPE html>
<html lang="en">
<head>
<meta charset="utf-8">
<title>Brestmoor Lab – Business Cards</title>
<link rel="stylesheet" href="https://fonts.googleapis.com/css2?family=Lato:wght@400;700;900&display=swap">
<style>
  :root {
    --brand-blue: #1a8ac6;
    --text-dark: #3a3a3a;
    --text-grey: #5a5a5a;
    --rule-grey: #9a9a9a;
    --card-white: #ffffff;
    --backdrop: #e6e2dc;
  }
  * { box-sizing: border-box; margin: 0; padding: 0; }
  html, body {
    width: 900px; height: 1200px; overflow: hidden;
    background: var(--backdrop);
    font-family: "Lato", Arial, sans-serif;
  }
  .canvas { position: relative; width: 900px; height: 1200px; }

  .card {
    position: absolute;
    background: var(--card-white);
    border-radius: 24px;
    box-shadow: 0 4px 10px rgba(0,0,0,0.25);
    overflow: hidden;
  }
  .card-front { left: 87px; top: 137px; width: 733px; height: 427px; }
  .card-front::after {
    content: ""; position: absolute; left: 0; right: 0; bottom: 0; height: 6px;
    background: var(--brand-blue);
  }
  .card-back { left: 87px; top: 632px; width: 734px; height: 431px; }

  .wordmark {
    position: absolute; display: flex; align-items: center;
    color: var(--brand-blue); font-weight: 900; text-transform: uppercase;
    letter-spacing: 0.5px; line-height: 1;
  }
  .wordmark .mark-dot { border-radius: 50%; background: var(--brand-blue); flex: none; }
  .card-front .wordmark { left: 28px; top: 82px; font-size: 34px; gap: 14px; }
  .card-front .wordmark .mark-dot { width: 30px; height: 30px; }
  .card-back .wordmark { left: 0; right: 0; top: 180px; justify-content: center; font-size: 52px; gap: 20px; }
  .card-back .wordmark .mark-dot { width: 46px; height: 46px; }

  .person-name {
    position: absolute; left: 26px; top: 226px;
    color: var(--brand-blue); font-size: 29px; font-weight: 700; letter-spacing: 0.3px;
  }
  .person-role {
    position: absolute; left: 26px; top: 264px;
    color: var(--text-dark); font-size: 16px;
  }
  .divider {
    position: absolute; left: 26px; top: 303px; width: 681px; height: 2px;
    background: var(--rule-grey);
  }
  .contact {
    position: absolute; display: flex; align-items: center; gap: 10px;
    color: var(--text-dark); font-size: 17px; letter-spacing: 0.3px;
  }
  .contact svg { flex: none; }
  .contact .social-dot { width: 16px; height: 16px; border-radius: 50%; background: var(--brand-blue); flex: none; margin: 0 2px 0 2px; }
  .contact-phone { left: 28px; top: 325px; }
  .contact-email { left: 28px; top: 357px; }
  .contact-social { left: 26px; top: 384px; }
  .contact-web { right: 26px; flex-direction: row; }
  .contact-web-1 { top: 357px; }
  .contact-web-2 { top: 384px; }

  .back-links {
    position: absolute; left: 0; right: 0; top: 376px; text-align: center;
    color: var(--text-grey); font-size: 18px; font-weight: 700;
  }
  .back-links .accent { color: var(--brand-blue); }
  .back-links .sep { margin: 0 14px; font-weight: 400; }
</style>
</head>
<body>
<div class="canvas">

  <section class="card card-front">
    <div class="wordmark"><span class="mark-dot"></span>Brestmoor Lab</div>

    <h1 class="person-name">TOMAS VRANA</h1>
    <p class="person-role">Data Platform Architect</p>
    <div class="divider"></div>

    <div class="contact contact-phone">
      <svg width="14" height="20" viewBox="0 0 14 20" aria-hidden="true">
        <rect x="1" y="1" width="12" height="18" rx="2" fill="none" stroke="var(--brand-blue)" stroke-width="2"/>
        <rect x="3.5" y="4" width="7" height="10" fill="var(--brand-blue)"/>
        <circle cx="7" cy="16.5" r="1" fill="var(--brand-blue)"/>
      </svg>
      <span>000 000 0000</span>
    </div>

    <div class="contact contact-email">
      <svg width="16" height="12" viewBox="0 0 16 12" aria-hidden="true">
        <rect x="0" y="0" width="16" height="12" fill="var(--brand-blue)"/>
        <path d="M0 0 L8 7 L16 0" fill="none" stroke="#fff" stroke-width="1.5"/>
      </svg>
      <span>tomas@brestmoorlab.cz</span>
    </div>

    <div class="contact contact-social">
      <span class="social-dot"></span>
      <span>@vranadata</span>
    </div>

    <div class="contact contact-web contact-web-1">
      <span>www.korvilnet.cz</span>
      <svg width="16" height="16" viewBox="0 0 16 16" aria-hidden="true">
        <g fill="none" stroke="var(--brand-blue)" stroke-width="1.2">
          <circle cx="8" cy="8" r="7"/><ellipse cx="8" cy="8" rx="3" ry="7"/>
          <line x1="1" y1="8" x2="15" y2="8"/><line x1="2.2" y1="4.5" x2="13.8" y2="4.5"/><line x1="2.2" y1="11.5" x2="13.8" y2="11.5"/>
        </g>
      </svg>
    </div>

    <div class="contact contact-web contact-web-2">
      <span>www.brestmoorlab.cz</span>
      <svg width="16" height="16" viewBox="0 0 16 16" aria-hidden="true">
        <g fill="none" stroke="var(--brand-blue)" stroke-width="1.2">
          <circle cx="8" cy="8" r="7"/><ellipse cx="8" cy="8" rx="3" ry="7"/>
          <line x1="1" y1="8" x2="15" y2="8"/><line x1="2.2" y1="4.5" x2="13.8" y2="4.5"/><line x1="2.2" y1="11.5" x2="13.8" y2="11.5"/>
        </g>
      </svg>
    </div>
  </section>

  <section class="card card-back">
    <div class="wordmark"><span class="mark-dot"></span>Brestmoor Lab</div>
    <p class="back-links">
      www.<span class="accent">korvilnet</span>.cz<span class="sep">|</span>www.<span class="accent">brestmoorlab</span>.cz
    </p>
  </section>

</div>
</body>
</html>
```